Business Cards and Stationery for CPA Firm
Gallowen & Company, P.C.
Business Cards and Stationery for CPA Firm -
Creative Brief
Professional
Bennett L. Gallowen
P.O. Box 482 9 West Cedar Ave. Pana, IL 62590
bgallowen@gallowencpa-example.com
www.gallowencpa-example.com
Need business cards and stationery for a CPA firm. I am open to design ideas and will provide feedback. Our generic email address for letterhead/fax is info@gallowencpa-example.com. This should be used in all locations except the business card. Each person with a business card will have his/her own email address.
Day - I've seen some with checkboxes for day of week. Other ideas welcome. Date Time Note

```html
<!DOCTYPE html>
<html lang="en">
<head>
<meta charset="utf-8">
<title>Gallowen &amp; Company, P.C. — Business Card</title>
<link rel="stylesheet" href="https://fonts.googleapis.com/css2?family=Cinzel:wght@500;600&family=Arimo:ital,wght@0,400;0,700;1,700&display=swap">
<style>
  :root {
    --backdrop: #e9e6e1;
    --card: #ffffff;
    --navy: #1c3d6b;
    --navy-deep: #0f2747;
    --navy-light: #3f6598;
    --ink: #2f3f52;
    --name-blue: #2b5b93;
    --rule: #1c3d6b;
  }
  * { margin: 0; padding: 0; box-sizing: border-box; }
  html, body {
    width: 1200px; height: 780px; overflow: hidden;
    background: var(--backdrop);
  }
  .canvas {
    position: relative; width: 1200px; height: 780px;
  }
  .card {
    position: absolute; left: 100px; top: 104px;
    width: 1000px; height: 572px;
    background: var(--card);
    border-radius: 34px;
    box-shadow: 0 10px 30px rgba(0,0,0,.18);
    overflow: hidden;
  }
  .band {
    position: absolute; left: 46px; top: 0; width: 128px; height: 100%;
    background: linear-gradient(90deg, var(--navy-deep), var(--navy) 45%, var(--navy-light) 75%, var(--navy));
    border-left: 3px solid #ffffff;
    border-right: 3px solid #ffffff;
    box-shadow: -6px 0 0 var(--navy), 6px 0 0 var(--navy);
  }
  .band-mark {
    position: absolute; top: 150px; left: 0; width: 100%;
    display: flex; flex-direction: column; align-items: center; gap: 10px;
  }
  .band-mark .dot {
    width: 14px; height: 14px; border: 2px solid #fff;
  }
  .band-mark .firm-word {
    font-family: "Arimo", sans-serif; font-weight: 400;
    font-size: 15px; letter-spacing: 1px; color: #ffffff;
  }
  .firm-title {
    position: absolute; left: 230px; top: 88px;
    font-family: "Cinzel", serif; font-weight: 600;
    font-size: 46px; color: var(--navy); letter-spacing: .5px;
    white-space: nowrap;
  }
  .firm-sub {
    position: absolute; left: 230px; top: 146px; width: 700px;
    display: flex; align-items: center; gap: 12px;
  }
  .firm-sub::before, .firm-sub::after {
    content: ""; height: 2px; background: var(--rule);
  }
  .firm-sub::before { width: 50px; }
  .firm-sub::after { flex: 1; }
  .firm-sub span {
    font-family: "Cinzel", serif; font-weight: 500;
    font-size: 15px; letter-spacing: 4px; color: var(--navy);
  }
  .address {
    position: absolute; left: 236px; top: 236px;
    font-family: "Arimo", sans-serif; font-size: 19px; line-height: 27px;
    color: var(--ink);
  }
  .contacts {
    position: absolute; left: 236px; top: 322px;
    list-style: none;
    font-family: "Arimo", sans-serif; font-size: 18px; color: var(--ink);
  }
  .contacts li {
    display: flex; align-items: center; gap: 10px; height: 32px;
  }
  .contacts svg { width: 18px; height: 18px; flex: none; }
  .person-name {
    position: absolute; left: 648px; top: 282px;
    font-family: "Arimo", sans-serif; font-weight: 700; font-style: italic;
    font-size: 27px; color: var(--name-blue);
  }
</style>
</head>
<body>
<main class="canvas">
  <article class="card">
    <div class="band">
      <div class="band-mark">
        <span class="dot"></span>
        <span class="firm-word">Gallowen</span>
      </div>
    </div>

    <h1 class="firm-title">Gallowen &amp; Company, P.C.</h1>
    <div class="firm-sub"><span>Certified Public Accountants</span></div>

    <address class="address">
      P.O. Box 482 9 West Cedar Ave.<br>
      Pana, IL 62590
    </address>

    <ul class="contacts">
      <li>
        <svg viewBox="0 0 20 20" aria-hidden="true"><path fill="#1c3d6b" d="M4 2l3 3-1.5 2.5c1 2.5 3 4.5 5.5 5.5L13.5 11l3 3-2 3C8 16 4 12 3 5.5z"/></svg>
        (217) 555-0148
      </li>
      <li>
        <svg viewBox="0 0 20 20" aria-hidden="true"><rect x="5" y="2" width="10" height="6" fill="#1c3d6b"/><rect x="2" y="8" width="16" height="7" rx="1" fill="#1c3d6b"/><rect x="5" y="13" width="10" height="5" fill="#fff" stroke="#1c3d6b" stroke-width="1.5"/></svg>
        (217) 555-0193
      </li>
      <li>
        <svg viewBox="0 0 20 20" aria-hidden="true"><circle cx="10" cy="10" r="8.5" fill="#1c3d6b"/><text x="10" y="14.5" text-anchor="middle" font-family="Arimo, sans-serif" font-size="13" font-weight="700" fill="#fff">@</text></svg>
        bgallowen@gallowencpa-example.com
      </li>
      <li>
        <svg viewBox="0 0 20 20" aria-hidden="true"><circle cx="10" cy="10" r="8.5" fill="none" stroke="#1c3d6b" stroke-width="1.8"/><ellipse cx="10" cy="10" rx="3.5" ry="8.5" fill="none" stroke="#1c3d6b" stroke-width="1.5"/><line x1="1.5" y1="10" x2="18.5" y2="10" stroke="#1c3d6b" stroke-width="1.5"/></svg>
        www.gallowencpa-example.com
      </li>
    </ul>

    <p class="person-name">Bennett L. Gallowen</p>
  </article>
</main>
</body>
</html>
```